LEARN Business Skills so you can Earn a good living

size of the poster is 8”x 10.75" plus 0.25" bleed.
Please leave 1 inch on the bottoum for footer
I want a design a poster that will attract people's attention.
I appreciate a creative ad however the ad should not take away from being able to clearly read the text.
-I also appreciate a simple creative ad that is not too busy.
-you can use graphics, vectors, or pictures of real people.
-however, if you use real people it should be a white male that is wearing a white shirt and look like a professional person.

Target Market(s)

Potential young business people

Industry/Entity Type

education

Requirements
Must have
• easy to read the text
Nice to have
• I would like a "creative" simple ad that is easy to be read
Should not have
• pictures of women

```html
<!DOCTYPE html>
<html lang="en">
<head>
<meta charset="utf-8">
<title>Business Enrichment Course Poster</title>
<link rel="stylesheet" href="https://fonts.googleapis.com/css2?family=Montserrat:wght@500;600;700;800&display=swap">
<style>
  :root {
    --sky: #00adee;
    --navy: #22264b;
    --paper: #ffffff;
    --backdrop: #e6e7e9;
    --photo-light: #f2f4f7;
    --photo-shade: #d9dee6;
  }
  * { margin: 0; padding: 0; box-sizing: border-box; }
  html, body {
    width: 1200px;
    height: 1000px;
    overflow: hidden;
    background: var(--backdrop);
    font-family: "Montserrat", sans-serif;
  }
  .stage {
    position: relative;
    width: 1200px;
    height: 1000px;
  }
  .poster-frame {
    position: absolute;
    left: 245px;
    top: 30px;
    width: 710px;
    height: 940px;
    overflow: hidden;
  }
  .poster {
    position: absolute;
    left: 0;
    top: 0;
    width: 1071px;
    height: 1418px;
    background: var(--paper);
    transform: scale(0.663);
    transform-origin: 0 0;
    overflow: hidden;
    color: var(--navy);
  }
  .poster-shapes {
    position: absolute;
    inset: 0;
    width: 1071px;
    height: 1418px;
  }
  .brand {
    position: absolute;
    left: 80px;
    top: 118px;
    display: flex;
    align-items: center;
    gap: 14px;
  }
  .brand-square {
    width: 22px;
    height: 22px;
    background: var(--sky);
  }
  .brand-name {
    font-weight: 700;
    font-size: 27px;
    line-height: 1.2;
    color: var(--sky);
    letter-spacing: 0.5px;
  }
  .headline {
    position: absolute;
    left: 76px;
    top: 305px;
    font-weight: 800;
    font-size: 61px;
    line-height: 101px;
  }
  .headline .accent { color: var(--sky); display: block; }
  .headline .dark { color: var(--navy); display: block; }
  .rule {
    position: absolute;
    height: 7px;
    background: var(--sky);
  }
  .rule--headline { left: 78px; top: 623px; width: 240px; }
  .rule--footer { left: 464px; top: 1289px; width: 142px; height: 5px; }
  .tagline {
    position: absolute;
    left: 79px;
    top: 680px;
    font-weight: 500;
    font-size: 31px;
    line-height: 46px;
  }
  .skills-band {
    position: absolute;
    left: 0;
    top: 805px;
    width: 766px;
    height: 60px;
    background: var(--sky);
    color: var(--paper);
    font-weight: 700;
    font-size: 30px;
    line-height: 60px;
    padding-left: 77px;
  }
  .benefit {
    position: absolute;
    display: flex;
    align-items: center;
    gap: 26px;
    font-weight: 500;
    font-size: 28px;
  }
  .benefit svg { width: 31px; height: 31px; flex: none; }
  .benefit--job { left: 129px; top: 893px; }
  .benefit--business { left: 486px; top: 893px; }
  .benefit--salary { left: 129px; top: 954px; }
  .topics {
    position: absolute;
    left: 40px;
    width: 990px;
    top: 1020px;
    text-align: center;
    font-weight: 600;
    font-size: 19px;
    line-height: 52px;
  }
</style>
</head>
<body>
<div class="stage">
  <div class="poster-frame">
    <div class="poster">
      <svg class="poster-shapes" viewBox="0 0 1071 1418" aria-hidden="true">
        <circle cx="650" cy="0" r="225" fill="var(--sky)"/>
        <circle cx="880" cy="-10" r="236" fill="var(--sky)" stroke="var(--paper)" stroke-width="30"/>
        <circle cx="1015" cy="533" r="370" fill="var(--sky)"/>
        <circle cx="955" cy="393" r="370" fill="var(--paper)"/>
        <circle cx="1107" cy="433" r="212" fill="var(--navy)"/>
        <path d="M612 230 A455 455 0 0 0 1052 721" fill="none" stroke="var(--sky)" stroke-width="13" stroke-linecap="round" stroke-dasharray="0 35.5"/>
      </svg>

      <svg class="poster-shapes" viewBox="0 0 1071 1418" role="img" aria-label="Photo of a smiling professional man in a white shirt with arms crossed">
        <defs>
          <linearGradient id="photoTone" x1="0" y1="0" x2="0" y2="1">
            <stop offset="0" stop-color="var(--photo-light)"/>
            <stop offset="1" stop-color="var(--photo-shade)"/>
          </linearGradient>
        </defs>
        <path d="M800 110 Q850 100 900 112 L905 270 Q990 300 1000 360 L1016 470 Q1000 560 960 570 L955 728 L730 728 L725 560 Q690 540 684 470 L690 360 Q700 300 800 270 Z" fill="url(#photoTone)"/>
      </svg>

      <div class="brand">
        <span class="brand-square"></span>
        <span class="brand-name">BRIGHTPATH<br>ACADEMY</span>
      </div>

      <h1 class="headline">
        <span class="accent">BUSINESS</span>
        <span class="accent">ENRICHMENT</span>
        <span class="dark">COURSE</span>
      </h1>
      <div class="rule rule--headline"></div>

      <p class="tagline">A proven success of<br>helping people in their livelihoods</p>

      <div class="skills-band">BUSINESS SKILLS THAT WILL HELP YOU :</div>

      <div class="benefit benefit--job">
        <svg viewBox="0 0 31 31"><rect width="31" height="31" fill="var(--sky)"/><path d="M6 15 L13 22 L25 9" fill="none" stroke="var(--paper)" stroke-width="4"/></svg>
        <span>Get a quality job</span>
      </div>
      <div class="benefit benefit--business">
        <svg viewBox="0 0 31 31"><rect width="31" height="31" fill="var(--sky)"/><path d="M6 15 L13 22 L25 9" fill="none" stroke="var(--paper)" stroke-width="4"/></svg>
        <span>Start/Grow your business</span>
      </div>
      <div class="benefit benefit--salary">
        <svg viewBox="0 0 31 31"><rect width="31" height="31" fill="var(--sky)"/><path d="M6 15 L13 22 L25 9" fill="none" stroke="var(--paper)" stroke-width="4"/></svg>
        <span>Increase your salary</span>
      </div>

      <p class="topics">
        BUSINESS ADMIISTRATION – SMALL BUSINESS MANAGEMENT - FINANCE - INVESTMENTS -<br>
        COMPUTERS- ACCOUNTING - SALES MARKETING - PROJECT MANAGEMENT INTERVIEWING<br>
        SKILLS - BUSINESS LAW -NEGOTIATION – PUBLIC SPEAKING - &nbsp;IMPORT/EXPORT -<br>
        INFORMATION TECHNOLOY -DISTRIBUTION - MARKETING - LEDGERLY - REAL ESTATE -<br>
        HEALTH CARE-MANAGEMENT - SHOPRIVER
      </p>
      <div class="rule rule--footer"></div>
    </div>
  </div>
</div>
</body>
</html>
```